Business Card Design

We sell fish products to corporate food companies who then turn these products into final food products for consumers

Industry/Entity Type

Business

Contact Information for Business Card

I need a corporate business card template for a fish products business. We would like it be professional for use in dealing with multi national companies. This company business card template will be used by multiple employees so the following fields must be open to edit (Name, Phone Number and Email address)

```html
<!DOCTYPE html>
<html lang="en">
<head>
<meta charset="utf-8">
<title>Coral Bay Seafoods – Business Card</title>
<link href="https://fonts.googleapis.com/css2?family=Open+Sans:wght@400;600&family=Saira+Condensed:wght@600;700&display=swap" rel="stylesheet">
<style>
  :root {
    --bg: #e9eaec;
    --card-white: #ffffff;
    --card-grey: #dcdde0;
    --navy: #0b4f9c;
    --navy-deep: #073f82;
    --teal: #1fa9c4;
    --green: #4cb87a;
    --ink-blue: #1f5ea8;
    --white: #ffffff;
  }
  * { box-sizing: border-box; margin: 0; padding: 0; }
  html, body {
    width: 1200px; height: 871px; overflow: hidden;
    background: var(--bg);
  }
  .canvas { position: relative; width: 1200px; height: 871px; }

  .card {
    position: absolute;
    width: 640px; height: 366px;
    overflow: hidden;
    box-shadow: 0 10px 28px rgba(0,0,0,0.18);
  }
  .card svg.band { position: absolute; inset: 0; width: 100%; height: 100%; }

  /* Back side */
  .card--back {
    left: 60px; top: 60px;
    background: linear-gradient(160deg, var(--card-grey) 0%, var(--card-white) 55%, var(--card-grey) 100%);
  }
  .card--back .wordmark {
    position: absolute; left: 0; right: 0; top: 92px;
    display: flex; flex-direction: column; align-items: center;
  }
  .card--back .website {
    position: absolute; left: 40px; bottom: 26px;
    font-family: "Saira Condensed", sans-serif; font-weight: 700;
    font-size: 19px; letter-spacing: 1.5px; color: var(--white);
    transform: rotate(-5deg); transform-origin: left bottom;
  }

  /* Wordmark */
  .wordmark .dot {
    width: 34px; height: 34px; border-radius: 50%;
    background: var(--teal); margin-bottom: 8px;
  }
  .wordmark .name {
    font-family: "Open Sans", sans-serif; font-weight: 600;
    color: var(--navy); text-align: center; line-height: 1.05;
    letter-spacing: 1px;
  }
  .card--back .wordmark .name { font-size: 34px; }

  /* Front side */
  .card--front {
    left: 500px; top: 445px;
    background: var(--card-white);
  }
  .card--front .holder {
    position: absolute; left: 44px; top: 118px;
    font-family: "Saira Condensed", sans-serif; font-weight: 700;
    font-size: 34px; letter-spacing: 2px; color: var(--ink-blue);
  }
  .contact-list {
    position: absolute; left: 44px; top: 180px;
    list-style: none;
    font-family: "Open Sans", sans-serif; font-size: 14px; color: var(--ink-blue);
  }
  .contact-list li { display: flex; align-items: center; gap: 12px; height: 24px; }
  .contact-list svg { width: 14px; height: 14px; fill: none; stroke: var(--green); stroke-width: 1.6; }
  .card--front .wordmark {
    position: absolute; left: 300px; top: 78px; width: 220px;
    display: flex; flex-direction: column; align-items: center;
  }
  .card--front .wordmark .name { font-size: 28px; }
</style>
</head>
<body>
<main class="canvas">

  <section class="card card--back" aria-label="Business card back">
    <svg class="band" viewBox="0 0 640 366" preserveAspectRatio="none" aria-hidden="true">
      <path d="M0,282 C210,300 430,262 640,150 L640,366 L0,366 Z" fill="var(--navy)"/>
      <path d="M110,288 C300,286 480,236 640,122 L640,146 C430,258 260,296 110,288 Z" fill="var(--teal)"/>
    </svg>
    <div class="wordmark">
      <span class="dot"></span>
      <span class="name">CORAL BAY<br>SEAFOODS</span>
    </div>
    <p class="website">WWW.CORALBAY.COM</p>
  </section>

  <section class="card card--front" aria-label="Business card front">
    <svg class="band" viewBox="0 0 640 366" preserveAspectRatio="none" aria-hidden="true">
      <path d="M548,0 C520,120 600,210 520,290 C495,318 478,345 470,366 L640,366 L640,0 Z" fill="var(--navy)"/>
      <path d="M528,0 C500,120 582,210 502,290 C478,318 462,345 454,366 L470,366 C478,345 495,318 520,290 C600,210 520,120 548,0 Z" fill="var(--teal)"/>
    </svg>
    <h1 class="holder">MARA ELLISON</h1>
    <ul class="contact-list">
      <li>
        <svg viewBox="0 0 16 16"><path d="M3 2 L6 2 L7 5 L5.5 6.5 C6.5 8.5 7.5 9.5 9.5 10.5 L11 9 L14 10 L14 13 C8 13 3 8 3 2 Z"/></svg>
        <span>555 014 2380</span>
      </li>
      <li>
        <svg viewBox="0 0 16 16"><rect x="4.5" y="1.5" width="7" height="13" rx="1.2"/><line x1="7" y1="12.2" x2="9" y2="12.2"/></svg>
        <span>555 014 2380</span>
      </li>
      <li>
        <svg viewBox="0 0 16 16"><rect x="1.5" y="3.5" width="13" height="9"/><path d="M1.5 3.5 L8 9 L14.5 3.5"/></svg>
        <span>mellison@coralbay.com</span>
      </li>
    </ul>
    <div class="wordmark">
      <span class="dot"></span>
      <span class="name">CORAL BAY<br>SEAFOODS</span>
    </div>
  </section>

</main>
</body>
</html>
```